Design required for boutique fire engineering firm in New Zealand

Our website was published based on free Wordpress templates, we'd like something a bit more bespoke, clean and simple.
Updates

Reason: didn't check this finished on a Sunday :)

Target Market(s)

architects, building owners, property developers

Industry/Entity Type

Boutique

Contact Information for Business Card

Logo
Fire Engineering

Desmond Harlow
Principal
+64 21 482 735
desmond@veltrane.nz
veltrane.nz

Number of Pages Required

3 page

Font styles to use
Sans Serif

Requirements
Nice to have
• On the business card, an embossed logo would be great - not sure if that's a design thing or just a print thing?
• Website, existing @ http://veltrane.nz for extent of content and general arrangement that I'm happy with.
• Ability to update the content with project bio's and some photos at a later date would be nice.

```html
<!DOCTYPE html>
<html lang="en">
<head>
<meta charset="utf-8">
<title>Veltrane — Consulting Fire Engineers</title>
<link href="https://fonts.googleapis.com/css2?family=Open+Sans:wght@400;600;700&display=swap" rel="stylesheet">
<style>
:root{
  --blue:#1f5fa8;
  --blue-mid:#2f6db5;
  --blue-soft:#3d77bb;
  --navy:#0e3f7c;
  --navy-deep:#0b3670;
  --ink:#2b3440;
  --muted:#6f87a6;
  --white:#ffffff;
}
*{margin:0;padding:0;box-sizing:border-box}
html,body{width:1200px;height:3400px;overflow:hidden;background:var(--white)}
body{font-family:"Open Sans",Arial,sans-serif;color:var(--ink);position:relative}
.abs{position:absolute}

/* hero */
.hero{left:0;top:0;width:1200px;height:660px;
  background:linear-gradient(180deg,#f3a35f 0%,#f6c28a 30%,#c8a08a 48%,#5d6f86 62%,#2c3b52 78%,#c7825a 92%,#7a5a4e 100%)}
.nav{left:160px;top:60px;width:920px;height:56px;display:flex;align-items:center;justify-content:space-between}
.brand{display:flex;align-items:center;gap:14px;font-size:34px;font-weight:700;color:var(--white)}
.brand-dot{width:40px;height:40px;border-radius:50%;background:var(--white)}
.nav-links{display:flex;gap:30px;font-size:17px;color:var(--white)}
.nav-links .active{font-weight:700}
.hero-title{left:160px;top:300px;font-size:72px;line-height:78px;font-weight:700;color:var(--white)}
.hero-sub{left:164px;top:456px;font-size:26px;font-weight:600;color:var(--white)}

/* intro */
.intro-heading{left:160px;top:810px;font-size:50px;line-height:56px;font-weight:700;color:var(--blue)}
.intro-text{left:160px;top:1010px;width:470px;font-size:22px;line-height:34px;color:var(--muted)}
.more{font-size:20px;font-weight:600;color:var(--blue);display:flex;align-items:center;gap:12px}
.intro-more{left:166px;top:1176px}
.firm-panel{left:760px;top:680px;width:440px;height:640px;background:linear-gradient(160deg,var(--blue-mid),var(--blue))}
.firm-body{left:800px;top:770px;color:var(--white)}
.firm-body h2{font-size:30px;font-weight:600;margin-bottom:28px}
.firm-body p{font-size:21px;line-height:30px}
.firm-body .more{color:var(--white);margin:26px 0 36px}

/* news */
.news-photo{left:160px;top:1300px;width:940px;height:440px;
  background:linear-gradient(100deg,#a8522a 0%,#c98a5a 30%,#e9e4e2 55%,#c9b5a2 80%,#8e5a36 100%)}
.news-card{left:600px;top:1540px;width:500px;height:320px;background:var(--navy);color:var(--white);padding:34px 40px}
.news-card .kicker{font-size:12px;font-weight:700;letter-spacing:1px}
.news-card h3{font-size:26px;line-height:32px;font-weight:700;margin:12px 0 14px}
.news-card p{font-size:14px;line-height:20px;opacity:.9}
.news-card .more{color:var(--white);margin-top:26px}

/* expertise */
.exp-heading{left:600px;top:1950px;font-size:44px;font-weight:700;color:var(--blue)}
.exp-image{left:160px;top:2020px;width:400px;height:280px;background:linear-gradient(135deg,#f4f5f8,#3c4a6b 55%,#f4f5f8)}
.exp-text{left:600px;top:2050px;width:480px;font-size:14px;line-height:21px;color:var(--muted)}
.exp-list{left:600px;top:2170px;list-style:none;font-size:22px;font-weight:600;color:var(--blue)}
.exp-list li{display:flex;align-items:center;gap:14px;height:36px}

/* testimonial */
.footer{left:0;top:2620px;width:1200px;height:780px;background:var(--navy-deep)}
.quote-band{left:0;top:2432px;width:1100px;height:328px;background:var(--blue-soft);color:var(--white);text-align:center}
.quote-avatar{left:530px;top:2462px;width:70px;height:70px;border-radius:50%;background:linear-gradient(#cfd6df,#8b97a6)}
.quote-text{left:250px;top:2556px;width:620px;font-size:25px;line-height:34px;text-align:center;color:var(--white)}
.quote-name{left:250px;top:2680px;width:620px;font-size:13px;text-align:center;color:var(--white)}
.quote-arrow{top:2566px}

/* footer */
.subscribe{left:160px;top:2800px;width:352px;height:56px;background:var(--blue-soft);color:var(--white);font-size:17px;display:flex;align-items:center;justify-content:center}
.socials{left:870px;top:2802px;display:flex;gap:16px}
.socials span{width:48px;height:48px;border-radius:50%;background:var(--blue-mid);display:block}
.rule{left:160px;width:880px;height:1px;background:rgba(255,255,255,.25)}
.foot-col{top:2960px;color:var(--white)}
.foot-col h4{font-size:18px;font-weight:700;margin-bottom:26px}
.foot-col p,.foot-col li{font-size:15px;line-height:24px;list-style:none}
.foot-col .strong{font-weight:700}
.legal{top:3346px;font-size:13px;color:var(--white)}
</style>
</head>
<body>

<div class="abs hero" role="img" aria-label="Sunset over a harbour with mountains and industrial chimneys"></div>
<header class="abs nav">
  <div class="brand"><span class="brand-dot"></span>veltrane</div>
  <nav class="nav-links"><span>Expertise</span><span class="active">Projects</span><span>Perspectives</span><span>Our Firm</span><span>Contact Us</span></nav>
</header>
<h1 class="abs hero-title">Consulting<br>Fire Engineers</h1>
<p class="abs hero-sub">based in Wellington, New Zealand</p>

<section>
  <div class="abs firm-panel"></div>
  <h2 class="abs intro-heading">Advanced<br>approach to<br>fire engineering</h2>
  <p class="abs intro-text">Veltrane is a boutique fire engineering firm based in Wellington, New Zealand, founded by Desmond Harlow in 2017.</p>
  <a class="abs more intro-more"><svg width="12" height="16" viewBox="0 0 12 16"><path d="M2 2l7 6-7 6" fill="none" stroke="currentColor" stroke-width="3"/></svg>Explore More</a>
  <div class="abs firm-body">
    <h2>Our Firm</h2>
    <p>14 Tasman Row<br>Kelburn Heights, WN 6012</p>
    <a class="more"><svg width="12" height="16" viewBox="0 0 12 16"><path d="M2 2l7 6-7 6" fill="none" stroke="currentColor" stroke-width="3"/></svg>Get Directions</a>
    <p>Lorem ipsum dolor sit amet,<br>consectetur adipiscing elit.<br>Phasellus non ante feugiat<br>purus lobortis convallis sed<br>ac mi. Vestibulum vitae fer-<br>mentum nisl.</p>
  </div>
</section>

<section>
  <div class="abs news-photo" role="img" aria-label="Speaker presenting to an audience in front of a projection screen"></div>
  <article class="abs news-card">
    <div class="kicker">RECENT FIRE NEWS</div>
    <h3>Guidance on<br>Fire Door Inspections &amp;<br>Maintenance</h3>
    <p>New national guidance sets clear steps for<br>checking, repairing and recording fire<br>doors in occupied commercial buildings.</p>
    <a class="more"><svg width="12" height="16" viewBox="0 0 12 16"><path d="M2 2l7 6-7 6" fill="none" stroke="currentColor" stroke-width="3"/></svg>Learn More</a>
  </article>
</section>

<section>
  <h2 class="abs exp-heading">Our Expertise</h2>
  <div class="abs exp-image" role="img" aria-label="Patterned navy necktie on a white background"></div>
  <p class="abs exp-text">Using advanced fire engineering techniques, our highly experienced Chartered Fire Engineers offer a complete overview of fire safety in order to provide design clarity with an alternative solution to strict code compliance.</p>
  <ul class="abs exp-list">
    <li><svg width="10" height="14" viewBox="0 0 10 14"><path d="M2 2l5 5-5 5" fill="none" stroke="currentColor" stroke-width="2.5"/></svg>Fire Safety Engineering</li>
    <li><svg width="10" height="14" viewBox="0 0 10 14"><path d="M2 2l5 5-5 5" fill="none" stroke="currentColor" stroke-width="2.5"/></svg>Passive Fire Protection</li>
    <li><svg width="10" height="14" viewBox="0 0 10 14"><path d="M2 2l5 5-5 5" fill="none" stroke="currentColor" stroke-width="2.5"/></svg>Fire Safety Management</li>
    <li><svg width="10" height="14" viewBox="0 0 10 14"><path d="M2 2l5 5-5 5" fill="none" stroke="currentColor" stroke-width="2.5"/></svg>Fire Expert Witness</li>
  </ul>
</section>

<footer>
  <div class="abs footer"></div>
  <div class="abs quote-band"></div>
  <div class="abs quote-avatar" role="img" aria-label="Client portrait"></div>
  <svg class="abs quote-arrow" style="left:196px" width="28" height="48" viewBox="0 0 28 48"><path d="M24 4L6 24l18 20" fill="none" stroke="#fff" stroke-width="6"/></svg>
  <svg class="abs quote-arrow" style="left:946px" width="28" height="48" viewBox="0 0 28 48"><path d="M4 4l18 20L4 44" fill="none" stroke="#fff" stroke-width="6"/></svg>
  <p class="abs quote-text">Maecenas diam mauris, mattis sed ante sed, pellentesque cursus libero. Mauris sit amet leo rhoncus, dapibus massa cursus, placerat augue.</p>
  <p class="abs quote-name">Mara Oaks, Director, Harbour Trust</p>

  <div class="abs subscribe">Subscribe to our Newsletter</div>
  <div class="abs socials"><span></span><span></span><span></span></div>
  <div class="abs rule" style="top:2910px"></div>

  <div class="abs foot-col" style="left:160px;width:190px">
    <h4>Support Us</h4>
    <p>Help us keep buildings safer by sharing our research and backing local fire safety work.</p>
    <ul style="margin-top:12px"><li class="strong">› Become a member</li><li class="strong">› Donate Now</li></ul>
  </div>
  <div class="abs foot-col" style="left:380px">
    <h4>Visit</h4>
    <ul><li>Plan a Visit</li><li>Map</li><li>Host an Event</li><li>Store</li></ul>
  </div>
  <div class="abs foot-col" style="left:608px">
    <h4>Explore</h4>
    <ul><li>What's New</li><li>Education</li><li>Experiences</li><li>About Us</li><li>Careers</li><li>Press</li></ul>
  </div>
  <div class="abs foot-col" style="left:832px">
    <h4>Location</h4>
    <p>14 Tasman Row<br>Kelburn Heights,<br>WN 6012</p>
  </div>

  <div class="abs rule" style="top:3320px"></div>
  <p class="abs legal" style="left:160px">© 2017 All rights reserved by veltrane</p>
  <p class="abs legal" style="left:800px;font-weight:700;word-spacing:2px">Privacy Policy &nbsp;|&nbsp; Terms of Use &nbsp;|&nbsp; Contact Us</p>
</footer>

</body>
</html>
```